依頼概要
■ 依頼の目的/概要

名前入りジュースのパッケージデザイン(ラベルデザイン)を依頼させて頂きます。

[お客様が指定できる項目]
1. ジュースの名前「○○の○○」
2. 送り主の名前
3. ハンコのアイコン

■ パッケージデザインへの要望

「安心」「安全」をパッケージから感じることができ、手作り感がありつつ高級感があるデザインを希望します。

■ 商品情報

商品は、お客様が名前を入れることができるジュースです。
北軽井沢で作られた天然果汁です。
種類は、プラム、りんご、なつはぜりんご、ブルーベリーの4種類です。
デザインは「プラム」をお願いします。残りの3つは決定したデザインを元にこちらでアレンジします。

■ ラベルの情報

サイズ:W150mm × H120mm(写真は添付資料参照)
印刷/カラー:フルカラー印刷

■ 納品ファイルの希望

イラストレーター形式もしくはフォトショップ形式

■ 進め方

弊社の希望するイメージに近い提案を1つ(場合によって複数)選択させて頂きます。希望に近づけるために、修正要望を個別にさせて頂くこともあります。コンペ方式のため、修正後に当選されない場合も、どうかご了承ください。

■ その他/注意点

名前入りジュースという特性のため、テキスト箇所は全てこちらで変更が可能なフォントをご利用いただくこととなります。
無料で商用利用が可能なフォントで選定してください。
(参考写真ではみかちゃんフォントを使用)

選択させて頂いたデザインの著作権(財産権)等の扱いはQuendry利用規約に従い、弊社に譲渡をお願いします。フォントや画像素材などを利用する場合は上記利用用途に使用できることを確認し、第三者の知的財産権等に注意して下さい。
■ 選んだ理由

軽井沢らしさを出して高級感があるデザインでした。

想定外の手書き文字による提案でしたが、手書き金額が商品売価調整可能範囲だったのが決定打でした。

■ 提案者全員へのお礼・コメント

たくさんのご応募ありがとうございました。

採用したのが依頼内容の「無料フォントを使ったもの」から外れていたのがルール違反だと思う方もいらっしゃるかもしれませんが、想定した内容にしばられない提案は、クライアントを良い意味で裏切り、時として抜きに出るものです。

今後の応募の参考になれば幸いです。

また募集することがあると思いますので、どうぞよろしくお願いいたします。

```html
<!DOCTYPE html>
<html lang="ja">
<head>
<meta charset="utf-8">
<title>美咲の誉れ — プラムジュース ラベル</title>
<link rel="stylesheet" href="https://fonts.googleapis.com/css2?family=Yuji+Syuku&display=swap">
<style>
  :root {
    --bg: #ffffff;
    --bottle-dark: #b83a1c;
    --bottle-mid: #d2522c;
    --bottle-light: #e27b52;
    --label: #ffffff;
    --ink: #1a1a1a;
    --seal: #c8281e;
    --fruit-orange: #ef8a4a;
    --fruit-red: #d92b22;
    --fruit-shadow: #f1e3c4;
  }
  * { margin: 0; padding: 0; box-sizing: border-box; }
  html, body {
    width: 1200px; height: 2464px; overflow: hidden;
    background: var(--bg);
  }
  .bottle {
    position: relative;
    width: 1200px; height: 2464px;
  }
  .bottle-shape { position: absolute; inset: 0; }
  .vertical {
    writing-mode: vertical-rl;
    position: absolute;
    color: var(--ink);
    font-family: "Yuji Syuku", serif;
    font-weight: 400;
    line-height: 1;
    white-space: nowrap;
  }
  .product-name {
    left: 522px; top: 770px;
    font-size: 140px;
    letter-spacing: 4px;
  }
  .origin-note {
    left: 806px; top: 800px;
    font-size: 30px;
    letter-spacing: 4px;
  }
  .sender {
    left: 376px; top: 1480px;
    font-size: 48px;
    letter-spacing: 4px;
  }
  .seal {
    position: absolute;
    left: 362px; top: 1712px;
    width: 76px; height: 84px;
    border: 5px solid var(--seal);
    border-radius: 6px;
  }
  .fruit-illustration {
    position: absolute;
    left: 470px; top: 1530px;
    width: 380px; height: 330px;
    border-radius: 46% 46% 44% 44%;
    background: radial-gradient(ellipse at 35% 55%, var(--fruit-orange) 0%, var(--fruit-red) 75%);
  }
</style>
</head>
<body>
  <main class="bottle">
    <svg class="bottle-shape" width="1200" height="2464" viewBox="0 0 1200 2464" aria-hidden="true">
      <defs>
        <linearGradient id="bottle-fill" x1="0" y1="0" x2="1" y2="0">
          <stop offset="0" stop-color="#b83a1c"/>
          <stop offset="0.45" stop-color="#d2522c"/>
          <stop offset="0.8" stop-color="#e27b52"/>
          <stop offset="1" stop-color="#d2522c"/>
        </linearGradient>
      </defs>
      <path d="M360 24 C450 8 750 8 840 24 C900 40 940 100 975 200 C995 280 1008 420 1008 720 H192 C192 420 205 280 225 200 C260 100 300 40 360 24 Z" fill="url(#bottle-fill)"/>
      <rect class="label" x="192" y="720" width="816" height="1220" fill="#ffffff"/>
      <path d="M192 1940 H1008 V2320 C1008 2380 975 2400 920 2400 H280 C225 2400 192 2380 192 2320 Z" fill="url(#bottle-fill)"/>
    </svg>

    <h1 class="vertical product-name">美咲の誉れ</h1>
    <p class="vertical origin-note">北軽井沢 天然果汁100%</p>
    <p class="vertical sender">社長より</p>
    <div class="seal" role="img" aria-label="送り主のハンコ"></div>
    <div class="fruit-illustration" role="img" aria-label="葉の付いたプラムの果実のイラスト"></div>
  </main>
</body>
</html>
```